World first health care product in tablet form to help save relationships and marriages

The product known as Zentharo is in tablet form 470mg and has 30 to a packet the packet size is approx 11cm in length x 4cm We want to use the color of the image attached for the package and cornflower blue for our name Zentharo. We also need to mention close to our name....... maintaining relationships with increased libido and desire ...... Our tablets are in a tamper-proof blister pack inserted into the package. We do not have a logo as yet, we are thinking of zen in small white letters and then THARO in large letters in cornflower blue or something a bit darker. (The O could also contain a smiley face) We are not that fussed with a logo as yet, maybe down the track if our product works and sells. As of today business in Australia has ground to a halt with this coronavirus and its as bad as you could imagine. Please help us make this new product work with a fabulous packet design.
Target Market(s)
females and males
Industry/Entity Type
Pharmaceutical
Requirements
Must have
- the colors of the images attached and cornflower blue

```html
<!DOCTYPE html>
<html lang="en">
<head>
<meta charset="utf-8">
<title>Zentharo – Pack Front</title>
<link href="https://fonts.googleapis.com/css2?family=Jost:wght@400;500&display=swap" rel="stylesheet">
<style>
  :root {
    --backdrop: #d2e3ea;
    --panel-white: #ffffff;
    --panel-shade: #eeeeee;
    --band-light: #9fdeeb;
    --band-deep: #6ec6da;
    --brand-teal: #2ea8c3;
    --ink: #333333;
    --white: #ffffff;
  }
  html, body {
    margin: 0;
    padding: 0;
    width: 1200px;
    height: 840px;
    overflow: hidden;
    background: var(--backdrop);
  }
  .canvas {
    position: relative;
    width: 1200px;
    height: 840px;
  }
  .pack-front {
    position: absolute;
    left: 100px;
    top: 200px;
    width: 1000px;
    height: 440px;
    display: flex;
    box-shadow: 0 18px 40px rgba(40, 80, 100, 0.18);
  }
  .label-area {
    position: relative;
    width: 700px;
    height: 100%;
    background: linear-gradient(135deg, var(--panel-white) 45%, var(--panel-shade) 100%);
  }
  .wordmark {
    position: absolute;
    left: 80px;
    top: 70px;
    margin: 0;
    font-family: "Jost", sans-serif;
    font-weight: 500;
    font-size: 112px;
    line-height: 1;
    letter-spacing: -1px;
    color: var(--brand-teal);
  }
  .wordmark sup {
    font-size: 18px;
    vertical-align: top;
    margin-left: 4px;
  }
  .tagline {
    position: absolute;
    left: 84px;
    top: 210px;
    margin: 0;
    font-family: "Jost", sans-serif;
    font-weight: 400;
    font-size: 24px;
    line-height: 1.3;
    color: var(--ink);
  }
  .pack-count {
    position: absolute;
    left: 84px;
    bottom: 48px;
    display: flex;
    align-items: center;
    gap: 12px;
    font-family: "Jost", sans-serif;
    font-weight: 500;
    font-size: 52px;
    color: var(--ink);
  }
  .capsule-icon {
    width: 64px;
    height: 44px;
  }
  .dosage-band {
    position: relative;
    width: 300px;
    height: 100%;
    background: linear-gradient(160deg, var(--band-light), var(--band-deep));
  }
  .cross-badge {
    position: absolute;
    left: 40px;
    top: 40px;
    width: 220px;
    height: 220px;
  }
  .strength {
    position: absolute;
    right: 36px;
    bottom: 40px;
    margin: 0;
    font-family: "Jost", sans-serif;
    font-weight: 400;
    font-size: 48px;
    color: var(--white);
  }
</style>
</head>
<body>
  <main class="canvas">
    <section class="pack-front">
      <div class="label-area">
        <h1 class="wordmark">Zentharo<sup>®</sup></h1>
        <p class="tagline">Maintaining Relationships With Increased<br>Libido And Desire</p>
        <div class="pack-count">
          <span>30</span>
          <svg class="capsule-icon" viewBox="0 0 64 44" aria-hidden="true">
            <rect x="4" y="6" width="22" height="34" rx="11" fill="var(--brand-teal)"/>
            <rect x="28" y="18" width="32" height="20" rx="10" fill="none" stroke="var(--brand-teal)" stroke-width="4"/>
          </svg>
        </div>
      </div>
      <div class="dosage-band">
        <svg class="cross-badge" viewBox="0 0 220 220" aria-hidden="true">
          <circle cx="110" cy="110" r="108" fill="var(--white)"/>
          <rect x="92" y="45" width="36" height="130" fill="var(--band-deep)"/>
          <rect x="45" y="92" width="130" height="36" fill="var(--band-deep)"/>
        </svg>
        <p class="strength">470mg</p>
      </div>
    </section>
  </main>
</body>
</html>
```